Palisade Lift Inc Website Deisgn

We are a new small elevator contracting company.
We would like a full website designed similar to
http://brightmorelift.com or https://www.northpeaklifting.ca/
In addition to contents found on the above webpages.. we would like a section for project gallery etc.... have fun with it ... make it professional

Target Market(s)

Elevator Consultants - Property managers - Condo Boards - Commercial office buildings

Coding

Coded - Design and coding required

Number of Pages Required

5+ page

Requirements
Must have
• Navigation Bar.. Be view able via mobile ..Should be pictures of Tall Office buildings in background.. Toronto city skyline etc....

Have Fun!

```html
<!DOCTYPE html>
<html lang="en">
<head>
<meta charset="utf-8">
<title>Palisade Lift Inc</title>
<link href="https://fonts.googleapis.com/css2?family=Outfit:wght@300;400;500;600;700;800;900&display=swap" rel="stylesheet">
<style>
:root{
  --red:#c8283e;
  --navy:#0b2553;
  --ink:#111111;
  --text:#3b3b3b;
  --grey-bg:#f6f6f6;
  --footer:#0e0f33;
  --line:#cfcfcf;
  --white:#ffffff;
}
*{box-sizing:border-box;margin:0;padding:0}
html,body{width:1200px;height:4003px;overflow:hidden;background:var(--white)}
body{position:relative;font-family:"Outfit",sans-serif;color:var(--text)}
.abs{position:absolute}

/* header */
.contact-chip{position:absolute;top:14px;display:flex;align-items:center;gap:14px}
.chip-icon{width:34px;height:34px;border:1.5px solid var(--red);border-radius:50%;display:flex;align-items:center;justify-content:center}
.chip-label{font-size:11px;letter-spacing:1.5px;color:var(--red);text-transform:uppercase}
.chip-value{font-size:15px;color:var(--ink);margin-top:3px}
.brand{position:absolute;top:10px;left:0;width:1200px;display:flex;justify-content:center;align-items:center;gap:8px}
.brand-mark{width:30px;height:30px;border:3px solid var(--ink);border-radius:50%}
.brand-name{font-size:25px;font-weight:800;color:var(--ink);letter-spacing:-.3px}
.main-nav{position:absolute;left:149px;top:67px;width:901px;height:43px;background:var(--navy);border-radius:6px;display:flex;align-items:center;padding-left:110px}
.main-nav a{color:var(--white);font-size:13.5px;text-decoration:none;position:relative;height:43px;line-height:43px;margin-right:62px}
.main-nav a:last-child{margin-right:0}
.main-nav a.active{color:#ff5a6e}
.main-nav a.active::after{content:"";position:absolute;left:0;right:0;bottom:0;height:3px;background:var(--red)}

/* hero */
.hero{position:absolute;left:0;top:126px;width:1200px;height:636px;background:linear-gradient(160deg,#6c7a7a 0%,#2f5a7e 35%,#356b98 60%,#4f8fbe 100%)}
.hero-tag{position:absolute;background:var(--red);color:var(--white);font-weight:700}
.hero-title{position:absolute;background:var(--navy);color:var(--white);font-weight:800}
.btn{position:absolute;display:flex;align-items:center;justify-content:center;color:var(--white);font-size:14px;border-radius:4px;text-decoration:none}
.btn-navy{background:var(--navy)}
.btn-red{background:var(--red)}

/* sections */
.section-title{position:absolute;left:0;width:1200px;text-align:center;font-size:45px;font-weight:800;color:var(--navy);letter-spacing:-.5px}
.section-title .hl{color:var(--red)}
.section-lead{position:absolute;left:0;width:1200px;text-align:center;font-size:13.5px;line-height:20px;color:var(--text)}

.service-card{position:absolute;width:393px;height:435px;border:1px solid var(--line);background:var(--white);border-radius:14px 14px 0 0;overflow:hidden;text-align:center}
.service-photo{height:180px;width:100%}
.service-card h3{font-size:27px;font-weight:800;color:var(--ink);margin-top:38px}
.service-card p{font-size:13.3px;line-height:20px;color:var(--text);margin:26px 34px 0}
.service-card a{display:block;margin-top:18px;font-size:13px;color:var(--red);text-decoration:none;font-weight:500}

.gallery-band{position:absolute;left:0;top:1985px;width:1200px;height:965px;background:var(--grey-bg)}
.gallery-grid{position:absolute;left:149px;top:2219px;width:901px;height:637px;display:grid;grid-template-columns:repeat(3,1fr);grid-template-rows:repeat(2,1fr)}
.gallery-cta{display:flex;align-items:center;justify-content:center;text-align:center;color:var(--white);font-size:34px;font-weight:800;line-height:52px;background:linear-gradient(150deg,#16305e 0%,#203f70 50%,#3a5a86 100%);box-shadow:0 20px 40px rgba(0,0,0,.15)}

/* form */
.field{position:absolute;border:1px solid #b9b9b9;border-radius:5px;font-size:12.5px;color:#6d6d6d;padding:14px 15px}
.field.tall{padding-top:16px}

/* footer */
.site-footer{position:absolute;left:0;top:3619px;width:1200px;height:384px;background:var(--footer);color:var(--white)}
.footer-brand{position:absolute;left:149px;top:70px;display:flex;align-items:center;gap:8px}
.footer-brand .brand-mark{border-color:var(--white);width:40px;height:40px}
.footer-brand .brand-name{color:var(--white);font-size:30px}
.about-box{position:absolute;left:149px;top:163px;width:252px;height:131px;background:var(--white);border-radius:6px;color:var(--ink);padding:18px 19px}
.about-box h4{font-size:12.5px;font-weight:700;margin-bottom:10px}
.about-box p{font-size:11.5px;line-height:18px}
.footer-col{position:absolute;top:72px}
.footer-col h4{font-size:20px;font-weight:500;margin-bottom:24px}
.footer-col li{list-style:none;font-size:13px;height:31px}
.info-row{display:flex;gap:19px;font-size:13px;line-height:22px;margin-bottom:14px}
.info-row svg{flex:none;margin-top:4px}
.footer-bottom{position:absolute;left:0;top:341px;width:1200px;border-top:1px solid #3a3b5c;height:43px;font-size:13px}
</style>
</head>
<body>

<header>
  <div class="contact-chip" style="left:149px">
    <div class="chip-icon"><svg width="14" height="10" viewBox="0 0 14 10"><rect x="0" y="0" width="14" height="10" rx="1.5" fill="#c8283e"/><path d="M1 1.5 7 6 13 1.5" stroke="#fff" stroke-width="1.3" fill="none"/></svg></div>
    <div><div class="chip-label">Drop us email</div><div class="chip-value">hello@palisadelift.com</div></div>
  </div>
  <div class="brand"><span class="brand-mark"></span><span class="brand-name">Palisade Lift Inc</span></div>
  <div class="contact-chip" style="left:900px">
    <div style="text-align:right"><div class="chip-label">Make a call</div><div class="chip-value">416-555-0182</div></div>
    <div class="chip-icon"><svg width="14" height="14" viewBox="0 0 24 24"><path d="M6.6 10.8a15.1 15.1 0 0 0 6.6 6.6l2.2-2.2a1 1 0 0 1 1-.25 11.4 11.4 0 0 0 3.6.57 1 1 0 0 1 1 1V20a1 1 0 0 1-1 1A17 17 0 0 1 3 4a1 1 0 0 1 1-1h3.5a1 1 0 0 1 1 1c0 1.25.2 2.45.57 3.57a1 1 0 0 1-.25 1z" fill="#c8283e"/></svg></div>
  </div>
  <nav class="main-nav">
    <a class="active" href="#">HOME</a>
    <a href="#">Our Services</a>
    <a href="#">Employees</a>
    <a href="#">FAQs</a>
    <a href="#">Free Quote</a>
    <a href="#">Contact Us</a>
  </nav>
</header>

<section class="hero" role="img" aria-label="Tall glass office towers seen from below against a blue sky"></section>
<div class="hero-tag" style="left:149px;top:252px;width:143px;height:47px;font-size:23px;padding:11px 20px">Welcome</div>
<div class="hero-title" style="left:149px;top:300px;width:571px;height:81px;font-size:56px;line-height:81px;padding-left:19px">Palisade Lift</div>
<div class="hero-tag" style="left:149px;top:381px;width:142px;height:81px;font-size:56px;font-weight:800;line-height:81px;padding-left:19px">INC</div>
<a class="btn btn-navy" href="#" style="left:149px;top:514px;width:135px;height:50px">Free Quote</a>
<a class="btn btn-red" href="#" style="left:291px;top:514px;width:135px;height:50px">Contact Us</a>

<h2 class="section-title" style="top:845px"><span class="hl">Services</span> We Offer</h2>
<p class="section-lead" style="top:910px">Lorem ipsum dolor sit amet, consectetur an adipiscing elit, sed do eiusmod tempor<br>incididunt ut labore man et dolore magna aliqua.</p>

<article class="service-card" style="left:188px;top:984px">
  <div class="service-photo" role="img" aria-label="Night view of a lit office building interior" style="background:linear-gradient(90deg,#2a2522,#7a5a3e 40%,#3a3430 70%,#1a1a1e)"></div>
  <h3>Modernization</h3>
  <p>Lorem ipsum dolor sit amet, consectetur adipiscing elit, sed do eiusmod tempor incididunt ut labore et dolore magna aliqua. Ut enim ad minim veniam, quis nostrud exercitation...</p>
  <a href="#">Free Quote</a>
</article>
<article class="service-card" style="left:619px;top:984px">
  <div class="service-photo" role="img" aria-label="Technician on ropes working on a glass facade" style="background:linear-gradient(120deg,#9fb4cf,#4e6f9c 50%,#b8c8dc)"></div>
  <h3>Maintenance</h3>
  <p>Lorem ipsum dolor sit amet, consectetur adipiscing elit, sed do eiusmod tempor incididunt ut labore et dolore magna aliqua. Ut enim ad minim veniam, quis nostrud exercitation...</p>
  <a href="#">Free Quote</a>
</article>
<article class="service-card" style="left:188px;top:1453px">
  <div class="service-photo" role="img" aria-label="Rows of wrenches hanging on a blue board" style="background:linear-gradient(180deg,#2b3d66,#1d2b4d 60%,#2c3550)"></div>
  <h3>Repairing</h3>
  <p>Lorem ipsum dolor sit amet, consectetur adipiscing elit, sed do eiusmod tempor incididunt ut labore et dolore magna aliqua. Ut enim ad minim veniam, quis nostrud exercitation...</p>
  <a href="#">Free Quote</a>
</article>
<article class="service-card" style="left:619px;top:1453px">
  <div class="service-photo" role="img" aria-label="Red ratchet tools on a dark surface" style="background:linear-gradient(120deg,#3a3a3e,#5a2a2e 45%,#d8313a 70%,#4a4a4e)"></div>
  <h3>Other Services</h3>
  <p>Lorem ipsum dolor sit amet, consectetur adipiscing elit, sed do eiusmod tempor incididunt ut labore et dolore magna aliqua. Ut enim ad minim veniam, quis nostrud exercitation...</p>
  <a href="#">Free Quote</a>
</article>

<div class="gallery-band"></div>
<h2 class="section-title" style="top:2070px"><span class="hl">Our Project</span> Gallery</h2>
<p class="section-lead" style="top:2148px">Lorem ipsum dolor sit amet, consectetur an adipiscing elit, sed do eiusmod tempor<br>incididunt ut labore man et dolore magna aliqua.</p>
<div class="gallery-grid">
  <div role="img" aria-label="Old brick lobby with an elevator door" style="background:linear-gradient(135deg,#5a3a2a,#3a2a22 50%,#c8c2b4)"></div>
  <div role="img" aria-label="Dark skyscraper among city towers" style="background:linear-gradient(180deg,#cfcfcf,#4a4a4a 45%,#2a2a2a 80%,#8a8a8a)"></div>
  <div role="img" aria-label="Warm hallway with framed pictures and an elevator" style="background:linear-gradient(120deg,#f2d2b0,#c48a5e 55%,#6a5a50)"></div>
  <div role="img" aria-label="Pink apartment tower with balconies" style="background:linear-gradient(135deg,#b88e98,#7a5a66 50%,#c7a0aa)"></div>
  <div role="img" aria-label="Atrium of a modern building with red floors" style="background:linear-gradient(180deg,#6a7a88,#2e3a46 55%,#7a2a2e)"></div>
  <div class="gallery-cta" role="img" aria-label="City skyline under a navy overlay"><span>View Project<br>Detail</span></div>
</div>

<h2 class="section-title" style="top:3030px"><span class="hl">Contact</span> Us</h2>
<p class="section-lead" style="top:3110px">Lorem ipsum dolor sit amet, consectetur an adipiscing elit, sed do eiusmod tempor<br>incididunt ut labore man et dolore magna aliqua.</p>
<form>
  <div class="field" style="left:214px;top:3184px;width:364px;height:44px">Name:</div>
  <div class="field" style="left:622px;top:3184px;width:363px;height:44px">Email Address:</div>
  <div class="field" style="left:214px;top:3246px;width:364px;height:44px">Phone Number:</div>
  <div class="field" style="left:622px;top:3246px;width:363px;height:44px">Problem/Issue:</div>
  <div class="field tall" style="left:214px;top:3308px;width:771px;height:128px">Message:</div>
  <a class="btn btn-navy" href="#" style="left:533px;top:3475px;width:134px;height:48px;font-size:13.5px">Send Message</a>
</form>

<footer class="site-footer">
  <div class="footer-brand"><span class="brand-mark"></span><span class="brand-name">Palisade Lift Inc</span></div>
  <div class="about-box">
    <h4>About Us</h4>
    <p>Lorem ipsum dolor sit amet, consectetur adipiscing elit, sed do eiusmod tempor incididunt ut labore et dolore magna aliqua.</p>
  </div>
  <div class="footer-col" style="left:476px">
    <h4>Quick Links</h4>
    <ul><li>Home</li><li>Our Services</li><li>Employees</li><li>FAQs</li><li>Free Quote</li><li>Contact Us</li></ul>
  </div>
  <div class="footer-col" style="left:690px">
    <h4>Others</h4>
    <ul><li>Lorem ipsum</li><li>Printing</li><li>Typesetting</li></ul>
  </div>
  <div class="footer-col" style="left:875px;top:75px">
    <h4>Contact Info</h4>
    <div class="info-row"><svg width="14" height="14" viewBox="0 0 24 24"><path d="M6.6 10.8a15.1 15.1 0 0 0 6.6 6.6l2.2-2.2a1 1 0 0 1 1-.25 11.4 11.4 0 0 0 3.6.57 1 1 0 0 1 1 1V20a1 1 0 0 1-1 1A17 17 0 0 1 3 4a1 1 0 0 1 1-1h3.5a1 1 0 0 1 1 1c0 1.25.2 2.45.57 3.57a1 1 0 0 1-.25 1z" fill="#c8283e"/></svg><span>416-555-0147</span></div>
    <div class="info-row"><svg width="14" height="14" viewBox="0 0 14 14"><rect x="1" y="5" width="12" height="8" rx="1.5" fill="#c8283e"/><path d="M2 5 4 1h6l2 4" fill="#c8283e"/><circle cx="7" cy="9" r="2" fill="#0e0f33"/></svg><span>(416) 555-0193</span></div>
    <div class="info-row"><svg width="14" height="10" viewBox="0 0 14 10"><rect width="14" height="10" rx="1.5" fill="#c8283e"/><path d="M1 1.5 7 6 13 1.5" stroke="#0e0f33" stroke-width="1.3" fill="none"/></svg><span>hello@palisadelift.com</span></div>
    <div class="info-row"><svg width="14" height="16" viewBox="0 0 14 18"><path d="M7 0a7 7 0 0 0-7 7c0 5 7 11 7 11s7-6 7-11a7 7 0 0 0-7-7z" fill="#c8283e"/><circle cx="7" cy="7" r="2.5" fill="#0e0f33"/></svg><span>Unit 12, 2210<br>Birchmount Row, Suite 9<br>ON M1X 0A0</span></div>
  </div>
  <div class="footer-bottom">
    <span class="abs" style="left:149px;top:14px">Privacy and Policy.</span>
    <span class="abs" style="right:150px;top:14px">© Copyright 2020. Palisade Lift INC</span>
  </div>
</footer>

</body>
</html>
```